VAMU, an e-commerce website with a twist, providing consumer-to-consumer and business-to-consumer sa

I have only uploaded 10 wire-frame pages of the website. These pages have been chosen for the different lay-outs and should give an idea of what will be needed. There are many more that I won’t upload yet, I aim to choose a winner first then there will be a high possibility that the winner will get the chance to do the design work for these later.
The design I have in mind is to keep it clean and easy with no/minimal fancy fonts and hieroglyphics. The logo is white with an orange highlight on a solid background of black, please note that the logo is white on a black background and is not a black box with white lettering, trust that makes sense. I like the idea of the top part of the website being black all the way across. I don’t see the need for more than 3 colours in the actual base website (the pictures and adverts added by users will add other colours). Although orange is the highlight colour in the logo I am open to suggestions on this, so long as the highlight colour features throughout the site.

Website width is 1220px, all pages in the PDF are 1220px

Logo font is Rezlong

The company is going to be like tradlo, but much more focused on raising money for charity and humanitarian relief.

Target Market(s)

the modern era of smartphones and the sharing community

Industry/Entity Type

Business

Number of Pages Required

5+ page

Font styles to use
Sans Serif
Other font styles liked:
• rezlong

Colors
faa54b
f78f20
ffffff
000000
fbfbfb
f5f5f5

Requirements
Nice to have
• Although orange is the highlight colour in the logo I am open to suggestions on this, so long as the highlight colour features throughout the site.

```html
<!DOCTYPE html>
<html lang="en">
<head>
<meta charset="utf-8">
<title>VAMU – Home</title>
<link rel="stylesheet" href="https://fonts.googleapis.com/css2?family=Open+Sans:wght@400;600;700&family=Comfortaa:wght@700&family=Roboto:wght@700;900&display=swap">
<style>
:root{
  --orange:#f78f20;
  --orange-light:#faa54b;
  --black:#000;
  --ink:#222;
  --white:#fff;
  --paper:#fbfbfb;
  --grey:#e3e3e3;
  --muted:#8a8a8a;
  --logo-grey:#9a9a9a;
}
*{box-sizing:border-box;margin:0;padding:0}
html,body{width:727px;height:1200px;overflow:hidden;background:var(--white)}
body{position:relative;font-family:"Open Sans",Arial,sans-serif;color:var(--ink)}
.abs{position:absolute}
.display{font-family:"Comfortaa",Arial,sans-serif;font-weight:700}

/* top bar */
.util-bar{left:0;top:0;width:727px;height:24px;background:#1d1d1d;color:#ddd;font-size:8.5px}
.util-bar a{position:absolute;top:7px;color:#ddd;text-decoration:none}
.util-bar .sep{position:absolute;top:0;width:1px;height:24px;background:#444}
.util-search{left:551px;top:0;width:147px;height:24px;background:#2c2c2c}
.util-search span{position:absolute;left:20px;top:7px}

/* header */
.masthead{left:0;top:24px;width:727px;height:73px;background:var(--black)}
.brand{left:29px;top:19px;color:var(--white);font-size:31px;font-weight:700;letter-spacing:-1px}
.nav-item{top:20px;width:100px;margin-left:-50px;text-align:center;color:var(--white);font-size:10.5px}
.nav-item svg{display:block;margin:0 auto 5px;width:16px;height:16px}

/* hero */
.video-tile{left:22px;width:194px;background:linear-gradient(135deg,#7d7a72,#4b4f52);color:var(--white);text-align:center;font-size:12.5px}
.video-tile .play{position:absolute;left:50%;margin-left:-21px;width:42px;height:42px}
.video-tile p{position:absolute;width:100%}

.search-panel{left:225px;top:111px;width:282px;height:278px;background:var(--orange);color:var(--white)}
.search-panel h2{position:absolute;left:21px;top:13px;font-size:17px}
.field-label{position:absolute;font-size:11.5px}
.field{position:absolute;height:24px;border:1px solid #fff3e0;font-size:10px;padding:5px 8px;color:#fff4e6}
.help{position:absolute;width:12px;height:12px;border-radius:50%;background:var(--orange-light);color:var(--white);font-size:8px;font-weight:700;text-align:center;line-height:12px}
.search-btn{position:absolute;left:21px;top:222px;width:247px;height:29px;background:linear-gradient(#333,#0a0a0a);color:var(--white);text-align:center;font-size:15px;line-height:29px}

.featured{left:513px;top:111px;width:194px;height:278px;border:1px solid #ccc;background:var(--white)}
.featured h2{height:33px;background:#f0f0f0;color:var(--orange);font-size:15px;padding:7px 16px}
.feat-item{position:absolute;left:15px;width:172px}
.feat-thumb{position:absolute;left:0;top:0;width:78px;height:62px;border:1px solid #ccc;background:linear-gradient(135deg,#e9e9e9,#9a9a9a)}
.feat-item h3{position:absolute;left:86px;top:0;font-size:9.5px;font-weight:600}
.feat-item p{position:absolute;left:86px;top:16px;width:86px;font-size:7.2px;line-height:12px;color:var(--muted)}
.feat-item a{position:absolute;left:86px;top:53px;font-size:7.5px;color:var(--orange);text-decoration:none}

/* training ad */
.course-ad{left:30px;top:404px;width:670px;height:69px;background:linear-gradient(90deg,#2a6fd6 0%,#2b87c9 45%,#2ea57a 80%,#2f9a3e 100%)}
.course-ad .badge{position:absolute;left:87px;top:9px;width:128px;height:50px;background:var(--white);font-size:12px;color:#555;padding:16px 0;text-align:center}
.course-ad ul{position:absolute;list-style:none;color:var(--white);font-size:8.5px;font-weight:700;line-height:14px}
.course-ad li::before{content:"\25B6";color:#f6c21c;font-size:6px;margin-right:4px;vertical-align:1px}

/* feedback */
.feedback{left:0;top:499px;width:727px;height:231px;background:var(--grey)}
.feedback .notch{position:absolute;left:350px;top:0;width:0;height:0;border-left:14px solid transparent;border-right:14px solid transparent;border-top:13px solid var(--white)}
.feedback h2{position:absolute;width:100%;top:24px;text-align:center;font-size:19px;color:#333}
.quote-card{position:absolute;top:63px;width:210px;height:120px;background:var(--white);padding:12px 18px 0 26px;font-size:8.8px;line-height:16px;color:#444}
.quote-card .q{position:absolute;left:20px;top:8px;font-size:16px;font-weight:700;font-style:italic}
.quote-card .qe{font-size:14px;font-weight:700;font-style:italic;line-height:0;vertical-align:-4px;margin-left:3px}
.quote-card .author{position:absolute;left:26px;top:82px;padding-left:30px;font-size:9px;line-height:12px}
.quote-card .author small{font-size:7.5px;color:#666}
.quote-card .avatar{position:absolute;left:0;top:0;width:24px;height:24px;border-radius:50%;background:#c9b8a8}
.cta{left:239px;top:712px;width:245px;height:31px;border-radius:16px;background:var(--orange);color:var(--white);font-size:11px;text-align:center;line-height:31px}

/* deals ad */
.deals-ad{left:34px;top:769px;width:664px;height:77px;background:linear-gradient(90deg,#f2b21c,#f7c531);border:1px solid #d08a10}
.deals-photo{position:absolute;left:18px;top:0;width:100px;height:75px;background:linear-gradient(135deg,#e7a56f,#c9485f)}
.deals-ad .h1{position:absolute;left:99px;top:10px;font-family:"Roboto",Arial,sans-serif;font-weight:900;font-size:13.5px;line-height:14px;color:#1a1a1a}
.deals-ad .h2{position:absolute;left:337px;top:15px;font-family:"Roboto",Arial,sans-serif;font-weight:900;font-size:21px;line-height:26px;color:#1a1a1a}
.deals-ad .btn{position:absolute;left:541px;top:17px;width:106px;height:26px;border-radius:3px;background:linear-gradient(#3f8cf0,#1d5fd0);border:1px solid #fff;color:var(--white);font-family:"Roboto",Arial,sans-serif;font-weight:700;font-size:13px;text-align:center;line-height:24px}
.deals-ad .corner{position:absolute;right:2px;top:1px;width:14px;height:11px;border:1px solid #3c8ce6;background:#fff}

/* charities */
.charities h2{position:absolute;left:35px;top:878px;font-size:17px;color:#333}
.charity{position:absolute;width:110px;text-align:center;color:var(--logo-grey);font-weight:700}
.charity .dot{display:block;margin:0 auto 4px;width:34px;height:34px;border-radius:50%;background:#cfcfcf}

.promo-yellow{left:373px;top:872px;width:325px;height:95px;background:radial-gradient(circle at 50% 40%,#fcd34a,#f6a816);text-align:center;color:var(--white)}
.promo-yellow .t{position:absolute;width:100%;top:22px;font-family:"Roboto",Arial,sans-serif;font-weight:900;font-size:14.5px;line-height:14px}
.promo-yellow .s{position:absolute;width:100%;top:68px;font-size:7px;color:#c24a12;line-height:10px}
.promo-teal{left:373px;top:978px;width:325px;height:96px;background:#2a9fb5;color:var(--white)}
.promo-photo{position:absolute;left:10px;top:0;width:90px;height:96px;background:linear-gradient(#3b5f68,#1d2d33)}
.promo-teal .t{position:absolute;left:113px;top:16px;font-family:"Roboto",Arial,sans-serif;font-weight:900;font-size:15px;line-height:17px}
.promo-teal .b{position:absolute;top:62px;height:19px;border:1px solid #e8f6f9;font-family:"Roboto",Arial,sans-serif;font-weight:700;font-size:9px;line-height:17px;text-align:center}

/* footer */
.footer{left:0;top:1107px;width:727px;height:93px;background:var(--orange);color:var(--white)}
.footer .links{position:absolute;left:42px;top:22px;font-size:11px}
.footer .links span{margin:0 6px}
.footer .copy{position:absolute;left:42px;top:50px;font-size:9.5px}
.footer .social{position:absolute;left:585px;top:22px}
.footer .social i{display:inline-block;width:14px;height:14px;border-radius:3px;background:var(--white);margin-left:4px}
.footer .meta{position:absolute;right:34px;top:54px;font-size:9.5px}
</style>
</head>
<body>

<div class="abs util-bar">
  <a style="left:29px">Notification</a><i class="sep" style="left:84px"></i>
  <a style="left:93px">News</a><i class="sep" style="left:124px"></i>
  <a style="left:132px">List Item</a>
  <a style="left:349px">Contact Us</a><i class="sep" style="left:401px"></i>
  <a style="left:410px">Help</a><i class="sep" style="left:438px"></i>
  <a style="left:446px">Terms and Conditions</a>
  <div class="abs util-search">
    <svg class="abs" style="left:9px;top:8px" width="9" height="9" viewBox="0 0 10 10"><circle cx="4" cy="4" r="3" fill="none" stroke="#ddd" stroke-width="1.5"/><path d="M6.3 6.3L9 9" stroke="#ddd" stroke-width="1.5"/></svg>
    <span>Search</span>
  </div>
</div>

<header class="abs masthead">
  <div class="abs brand">VAMU</div>
  <div class="abs nav-item" style="left:327px">
    <svg viewBox="0 0 16 16"><path d="M2 6h12l-1.5 8h-9z" fill="#fff"/><path d="M5 6l3-4 3 4" fill="none" stroke="#fff" stroke-width="1.4"/></svg>Shopping Basket</div>
  <div class="abs nav-item" style="left:411px">
    <svg viewBox="0 0 16 16"><path d="M8 14L2 8a3.3 3.3 0 0 1 6-4 3.3 3.3 0 0 1 6 4z" fill="#fff"/></svg>Wish list</div>
  <div class="abs nav-item" style="left:470px">
    <svg viewBox="0 0 16 16"><rect x="3" y="7" width="10" height="8" fill="#fff"/><path d="M5 7V5a3 3 0 0 1 6 0v2" fill="none" stroke="#fff" stroke-width="1.6"/></svg>Sign In</div>
  <div class="abs nav-item" style="left:538px">
    <svg viewBox="0 0 16 16"><circle cx="8" cy="5" r="3.5" fill="#fff"/><path d="M2 15a6 5 0 0 1 12 0z" fill="#fff"/></svg>My Account</div>
  <div class="abs nav-item" style="left:638px">
    <svg viewBox="0 0 16 16"><circle cx="7" cy="7" r="4.5" fill="none" stroke="#fff" stroke-width="2"/><path d="M10.5 10.5L14 14" stroke="#fff" stroke-width="2"/></svg>My Recent Searches</div>
</header>

<section class="abs video-tile" style="top:111px;height:133px" role="img" aria-label="Video still: smiling man working on a laptop">
  <svg class="play" style="top:34px" viewBox="0 0 42 42"><circle cx="21" cy="21" r="19" fill="none" stroke="#fff" stroke-width="2.5"/><path d="M16 12l12 9-12 9z" fill="#fff"/></svg>
  <p style="top:90px">What it's about</p>
</section>
<section class="abs video-tile" style="top:255px;height:134px;background:linear-gradient(135deg,#8b8f80,#4f5a4a)" role="img" aria-label="Video still: hands stacked together in support">
  <svg class="play" style="top:30px" viewBox="0 0 42 42"><circle cx="21" cy="21" r="19" fill="none" stroke="#fff" stroke-width="2.5"/><path d="M16 12l12 9-12 9z" fill="#fff"/></svg>
  <p style="top:84px">What VAMU does for charity</p>
</section>

<section class="abs search-panel">
  <h2 class="display">search your product</h2>
  <span class="field-label" style="left:20px;top:43px">Product</span>
  <div class="field" style="left:20px;top:63px;width:230px">Items</div><span class="help" style="left:256px;top:69px">?</span>
  <span class="field-label" style="left:20px;top:95px">Location</span>
  <div class="field" style="left:20px;top:114px;width:230px">location</div><span class="help" style="left:256px;top:120px">?</span>
  <span class="field-label" style="left:20px;top:156px">From</span>
  <div class="field" style="left:59px;top:150px;width:192px">£</div><span class="help" style="left:256px;top:156px">?</span>
  <span class="field-label" style="left:20px;top:188px">To</span>
  <div class="field" style="left:59px;top:183px;width:192px;color:#fbb56a">£</div><span class="help" style="left:256px;top:188px">?</span>
  <div class="search-btn display">search</div>
</section>

<aside class="abs featured">
  <h2 class="display">featured product</h2>
  <div class="feat-item" style="top:45px">
    <div class="feat-thumb" role="img" aria-label="Product photo: compact camcorder"></div>
    <h3>Item Tittle here</h3><p>Praesent elementum elit at tellus nec ultri cies sit amet</p><a>CLICK HERE</a>
  </div>
  <div class="feat-item" style="top:122px">
    <div class="feat-thumb" role="img" aria-label="Product photo: dark tablet case"></div>
    <h3>Item Tittle here</h3><p>Praesent elementum elit at tellus nec ultri cies sit amet</p><a>CLICK HERE</a>
  </div>
  <div class="feat-item" style="top:200px">
    <div class="feat-thumb" role="img" aria-label="Product photo: white VR headset" style="background:linear-gradient(135deg,#f4f4f4,#bdbdbd)"></div>
    <h3>Item Tittle here</h3><p>Praesent elementum elit at tellus nec ultri cies sit amet</p><a>CLICK HERE</a>
  </div>
</aside>

<section class="abs course-ad">
  <div class="badge">Brindlecast Ads</div>
  <ul style="left:243px;top:15px"><li>Quality Instructors</li><li>Live Training</li><li>Small Classes</li></ul>
  <ul style="left:390px;top:15px"><li>Hands-on Learning</li><li>Excellent Student Reviews</li><li>Free Retakes</li></ul>
</section>

<section class="abs feedback">
  <span class="notch"></span>
  <h2 class="display">user feedback</h2>
  <article class="quote-card" style="left:41px"><span class="q">"</span>Praesent elementum elit at tellus nec ultricies sit amet porttitor mattis enim In massa libero interdum nec interdum vel blandit sed nulla In ullamcorper<span class="qe">"</span>
    <div class="author"><span class="avatar" role="img" aria-label="Reviewer portrait"></span>By Author Name<br><small>Location City</small></div></article>
  <article class="quote-card" style="left:261px"><span class="q">"</span>Praesent elementum elit at tellus nec ultricies sit amet porttitor mattis enim In massa libero interdum nec interdum vel blandit sed nulla In <span class="qe">"</span>
    <div class="author"><span class="avatar" role="img" aria-label="Reviewer portrait" style="background:#a9a49c"></span>By Author Name<br><small>Location City</small></div></article>
  <article class="quote-card" style="left:481px"><span class="q">"</span>Praesent elementum elit at tellus nec ultricies sit amet porttitor mattis enim In massa libero interdum nec interdum vel blandit sed nulla In ullamcorper<span class="qe">"</span>
    <div class="author"><span class="avatar" role="img" aria-label="Reviewer portrait" style="background:#d8b9a0"></span>By Author Name<br><small>Location City</small></div></article>
</section>
<div class="abs cta">Leave feedback for a chance to win a price</div>

<section class="abs deals-ad">
  <div class="deals-photo" role="img" aria-label="Advert photo: shopper holding colourful bags"></div>
  <div class="h1">Find Exclusive Deals<br>Here!</div>
  <div class="h2">Up to 70%<br>off!</div>
  <div class="btn">Learn More</div>
  <span class="corner"></span>
</section>

<section class="charities">
  <h2 class="display">charities support</h2>
  <div class="charity" style="left:22px;top:922px;font-size:8px"><span class="dot"></span>YOUTH CIRCLE CLUBS</div>
  <div class="charity" style="left:136px;top:922px;font-size:11px"><span class="dot"></span>KindLife</div>
  <div class="charity" style="left:249px;top:940px;font-size:22px;font-weight:400">Hearthold</div>
  <div class="charity" style="left:22px;top:1000px;font-size:9px"><span class="dot" style="width:40px;height:40px"></span>LIFT FOUNDATION</div>
  <div class="charity" style="left:136px;top:1000px;font-size:11px"><span class="dot" style="width:40px;height:40px"></span>Paws Trust</div>
  <div class="charity" style="left:249px;top:1000px;font-size:11px"><span class="dot" style="width:40px;height:40px"></span>Relief Guild</div>
</section>

<section class="abs promo-yellow">
  <div class="t">BRING IDEAS TO LIFE<br>ACROSS SCREENS</div>
  <div class="s">THREE STANDARD SIZES<br>728X90 • 300X250 • 160X600</div>
</section>
<section class="abs promo-teal">
  <div class="promo-photo" role="img" aria-label="Advert photo: businesswoman in glasses"></div>
  <div class="t">BUSINESS AD EXPANDABLE<br>WITH QUILLORA</div>
  <div class="b" style="left:114px;width:52px">▶ VIDEO</div>
  <div class="b" style="left:175px;width:98px;background:#1f7f92">PSD INCLUDED</div>
</section>

<footer class="abs footer">
  <div class="links">About VAMU<span>|</span>Safety Hub<span>|</span>Resolution Hub<span>|</span>Vendor Hub<span>|</span>Partner Hub<span>|</span>Chairty Hub</div>
  <div class="copy">© 2017 Company Name&nbsp; All right reserved</div>
  <div class="social"><i></i><i></i><i></i><i></i><i></i><i></i></div>
  <div class="meta">Advertise&nbsp; |&nbsp; Sitemap</div>
</footer>

</body>
</html>
```